Flyer Design Print Ad for Clothing Store

We are a modest women's clothing store. We are looking for a print ad 90*134 mm that is attention grabbing and can serve as a template for us going forward. We cannot use pictures of actual women. We need it to include our logo, store hours, physical address, website, phone number. We would use this template and change the call to action as necessary e. g. BOGO Sale, 30% off, flash sale, summer sale etc. Our colors are black and white and our fonts are Bodoni sans and Athens.

Target Market(s)

Women from teen to age 70

Industry/Entity Type

Women's clothing

Font styles to use
Other font styles liked:
• Athens, Bodoni Sans

Requirements
Must have
• Our, logo, phone number, website, address and store hours
Nice to have
• I'd like something that's not just our flat logo but something that will make someone pause to look
Should not have
• Pictures of women

```html
<!DOCTYPE html>
<html lang="he">
<head>
<meta charset="utf-8">
<title>Alloria – Flash Sale</title>
<link href="https://fonts.googleapis.com/css2?family=Bodoni+Moda:wght@400&family=Montserrat:wght@600&family=Raleway:wght@300;400&family=Heebo:wght@400;700&display=swap" rel="stylesheet">
<style>
  :root {
    --ink: #111111;
    --paper: #ffffff;
    --pattern: #e6e6e6;
    --rule: #222222;
    --divider: #999999;
  }
  * { margin: 0; padding: 0; box-sizing: border-box; }
  html, body { width: 806px; height: 1200px; overflow: hidden; background: var(--paper); }
  .flyer { position: relative; width: 806px; height: 1200px; background: var(--paper); color: var(--ink); }

  .brand-mark {
    position: absolute; left: 274px; top: 82px; width: 258px; height: 258px;
    border-radius: 50%; background: var(--ink);
  }
  .brand-name {
    position: absolute; left: 0; right: 0; top: 386px; text-align: center;
    font-family: "Bodoni Moda", serif; font-weight: 400; font-size: 60px;
    letter-spacing: 22px; padding-left: 22px; line-height: 1;
  }
  .contact-line {
    position: absolute; left: 0; right: 0; top: 503px; text-align: center;
    font-family: "Raleway", sans-serif; font-weight: 300; font-size: 24px;
    font-variant-numeric: lining-nums;
    direction: ltr; white-space: nowrap;
  }
  .contact-line .sep { color: var(--divider); margin: 0 16px; }
  .contact-line .days-he { font-family: "Heebo", sans-serif; font-weight: 700; margin: 0 12px 0 4px; }

  .pattern-strip {
    position: absolute; top: 652px; width: 72px; height: 129px; background: var(--pattern);
  }
  .pattern-strip.left { left: 0; }
  .pattern-strip.right { right: 0; }

  .offer-frame {
    position: absolute; left: 82px; top: 623px; width: 641px; height: 186px;
    border: 1.5px solid var(--rule); border-top: none;
  }
  .offer-frame .top-rule { position: absolute; top: 0; height: 1.5px; background: var(--rule); }
  .offer-frame .top-rule.left { left: 0; width: 60px; }
  .offer-frame .top-rule.right { right: 0; width: 58px; }
  .offer-kicker {
    position: absolute; left: 0; right: 0; top: -8px; text-align: center;
    font-family: "Montserrat", sans-serif; font-weight: 600; font-size: 38px;
    letter-spacing: 24px; padding-left: 24px; line-height: 1;
  }
  .offer-amount {
    position: absolute; left: 0; right: 0; top: 48px; text-align: center;
    font-family: "Bodoni Moda", serif; font-weight: 400; font-size: 106px; line-height: 1;
  }

  .location { position: absolute; left: 0; right: 0; top: 880px; text-align: center; font-style: normal; }
  .location-he {
    font-family: "Heebo", sans-serif; font-weight: 700; font-size: 41px; line-height: 49px;
  }
  .location-en {
    font-family: "Raleway", sans-serif; font-weight: 400; font-size: 27px; line-height: 30px; margin-top: 2px;
  }
  .location-note {
    font-family: "Heebo", sans-serif; font-weight: 700; font-size: 24px; line-height: 36px; margin-top: 12px;
  }
  .location-alt {
    font-family: "Heebo", sans-serif; font-weight: 700; font-size: 25px; line-height: 36px; margin-top: 2px;
  }
  .bus-lines {
    font-family: "Raleway", sans-serif; font-weight: 400; font-size: 18px; line-height: 24px; margin-top: 1px;
    font-variant-numeric: lining-nums; direction: ltr;
  }

  .footer-band {
    position: absolute; left: 0; right: 0; bottom: 0; height: 74px; background: var(--ink);
    color: var(--paper); display: flex; align-items: center; justify-content: center;
    font-family: "Raleway", sans-serif; font-weight: 400; font-size: 26px; direction: ltr;
  }
</style>
</head>
<body>
<main class="flyer">
  <div class="brand-mark" aria-hidden="true"></div>
  <h1 class="brand-name" dir="ltr">ALLORIA</h1>

  <p class="contact-line">
    <span class="phone">077-5550142</span><span class="sep">|</span><span class="hours">S-Th-10:00-13:00-</span><span class="days-he" dir="rtl">א-ה</span><span class="hours">19:00-22:00</span>
  </p>

  <div class="pattern-strip left" role="img" aria-label="Soft grey repeating floral pattern"></div>
  <div class="pattern-strip right" role="img" aria-label="Soft grey repeating floral pattern"></div>

  <section class="offer-frame">
    <span class="top-rule left"></span>
    <span class="top-rule right"></span>
    <p class="offer-kicker" dir="ltr">FLASH SALE</p>
    <p class="offer-amount" dir="ltr">30% OFF</p>
  </section>

  <address class="location">
    <p class="location-he" dir="rtl">מרכז מסחרי גבעת הדר</p>
    <p class="location-en" dir="ltr">Givat Hadar Shopping Center</p>
    <p class="location-note" dir="rtl">(מעל קפה לימון)</p>
    <p class="location-alt" dir="rtl">ניתן להגיע גם משדרות הדר 16</p>
    <p class="bus-lines">Buses 14, 18, 27, 33, 40, 48, 56, 61, 72, 74, 80</p>
  </address>

  <footer class="footer-band">www.Alloria.co.il</footer>
</main>
</body>
</html>
```